Hearth Bloom Workshop needs a brochure designed.

Larkfen Studio is an interior design firm based in Sydney. We will be running Hearth Bloom Workshops
for all people interested in learning how to decorate
their home. It is important to show modern interior images to attract and excite their creative juices!
Colours we would like is a dark charcoal background
with Chartreuse trim for our logo and for the brochure.
We have attached some of our ideas on wording.
Our images can be replaced or changed to suit your
design.
The final design should be very stylish and to instill a desire to attend our workshops!

Target Market(s)

Mainly female adults in Sydney, aged approx. 25 to 60, who are interested in
interior decorating their homes.

Industry/Entity Type

Learning

Colors
5c5c5c
acd036

Requirements
Must have
• Must show good visual images to catch attention.
Nice to have
• Page layout i.e. to uploaded document, but open to any designs that work better.

```html
<!DOCTYPE html>
<html lang="en">
<head>
<meta charset="utf-8">
<title>Hearth Bloom Workshop Brochure</title>
<link rel="stylesheet" href="https://fonts.googleapis.com/css2?family=Arimo:wght@400;700&family=Raleway:wght@300&display=swap">
<style>
  :root {
    --page-bg: #e4e5e6;
    --charcoal: #5c5c5c;
    --charcoal-deep: #4f4f50;
    --chartreuse: #acd036;
    --text-light: #f2f2f2;
    --photo-wall: #c9cbc8;
    --photo-floor: #6f6e6c;
  }
  * { box-sizing: border-box; margin: 0; padding: 0; }
  html, body { width: 1200px; height: 800px; overflow: hidden; }
  body {
    background: radial-gradient(ellipse at center, #f2f2f3 0%, var(--page-bg) 70%, #cfd0d1 100%);
    font-family: "Arimo", Arial, sans-serif;
    position: relative;
  }
  .brochure {
    position: absolute;
    left: 150px; top: 90px;
    width: 900px; height: 620px;
    display: flex;
    box-shadow: 0 18px 40px rgba(0,0,0,0.25);
  }
  .panel {
    position: relative;
    width: 300px; height: 100%;
    background: var(--charcoal);
    border-top: 14px solid var(--chartreuse);
    border-bottom: 14px solid var(--chartreuse);
    overflow: hidden;
  }
  .panel--middle { background: var(--charcoal-deep); }
  .photo { display: block; width: 100%; }
  .photo--living { height: 330px; background: linear-gradient(180deg, var(--photo-wall) 0%, #b3b4b1 55%, var(--photo-floor) 100%); }
  .photo--lounge { height: 270px; background: linear-gradient(180deg, #d9dbd8 0%, #c2c4c0 50%, #8d8c88 100%); }
  .photo--bedroom { position: absolute; left: 0; bottom: 0; height: 170px; background: linear-gradient(180deg, #d8d3ca 0%, #b9ad9b 60%, #8a7f70 100%); }
  .intro {
    padding: 34px 30px 0;
    text-align: center;
    color: var(--text-light);
    font-size: 13.5px;
    line-height: 1.75;
  }
  .story {
    padding: 26px 22px 0;
    text-align: justify;
    color: var(--text-light);
    font-size: 13px;
    font-weight: 700;
    line-height: 1.6;
  }
  .learn { padding: 26px 22px 0; color: var(--text-light); }
  .learn__title {
    font-family: "Raleway", Arial, sans-serif;
    font-weight: 300;
    font-size: 25px;
    letter-spacing: 1px;
    color: var(--chartreuse);
    margin-bottom: 16px;
  }
  .learn__list { list-style: none; }
  .learn__item {
    position: relative;
    padding-left: 14px;
    margin-bottom: 12px;
    font-size: 11.5px;
    line-height: 1.35;
    text-align: justify;
  }
  .learn__item svg { position: absolute; left: 0; top: 3px; }
  .learn__note {
    margin-top: 22px;
    font-size: 12px;
    line-height: 1.55;
  }
</style>
</head>
<body>
  <main class="brochure">
    <section class="panel panel--left">
      <div class="photo photo--living" role="img" aria-label="Modern living room with a television on a timber console and a yellow armchair"></div>
      <p class="intro">
        Would you like to transform your home?<br>
        Do you feel OVERWHELMED and CONFUSED as to Where to start?<br>
        Are you unsure of a colour scheme, what type of furniture, Soft furnishings, accessories suit your home and lifestyle?<br>
        Where to buy?<br>
        What will suit your budget?
      </p>
    </section>

    <section class="panel panel--middle">
      <div class="photo photo--lounge" role="img" aria-label="Bright lounge with a white sofa, yellow cushions and a round coffee table"></div>
      <p class="story">
        Tess Warrick and Nadia Holt of LARKFEN STUDIO Interior Design understand the frustration and confusion that D.I.Y. home decorators face and will be holding HEARTH BLOOM WORKSHOPS in which you will learn how to create innovative colour schemes and styles from concept to completion in a fun, hands on experience, surrounded by beautiful furniture, fabrics, soft furnishings and homewares that will get your creative juices flowing!
      </p>
    </section>

    <section class="panel panel--right">
      <div class="learn">
        <h2 class="learn__title">YOU WILL LEARN</h2>
        <ul class="learn__list">
          <li class="learn__item"><svg width="7" height="8" viewBox="0 0 7 8"><path d="M0 0L7 4L0 8Z" fill="var(--chartreuse)"/></svg>Where and how to use colour, shape, form, and different textures to create a balanced and harmonious environment.</li>
          <li class="learn__item"><svg width="7" height="8" viewBox="0 0 7 8"><path d="M0 0L7 4L0 8Z" fill="var(--chartreuse)"/></svg>Current styles and what inspires you.</li>
          <li class="learn__item"><svg width="7" height="8" viewBox="0 0 7 8"><path d="M0 0L7 4L0 8Z" fill="var(--chartreuse)"/></svg>Space planning and furniture placement for your room to give a balanced and spacious feel.</li>
          <li class="learn__item"><svg width="7" height="8" viewBox="0 0 7 8"><path d="M0 0L7 4L0 8Z" fill="var(--chartreuse)"/></svg>Where to start!</li>
          <li class="learn__item"><svg width="7" height="8" viewBox="0 0 7 8"><path d="M0 0L7 4L0 8Z" fill="var(--chartreuse)"/></svg>How to bring it all together with the finishing touches.</li>
          <li class="learn__item"><svg width="7" height="8" viewBox="0 0 7 8"><path d="M0 0L7 4L0 8Z" fill="var(--chartreuse)"/></svg>Why Concept plans and mood boards are important.</li>
        </ul>
        <p class="learn__note">You will also enjoy making your very own mood board which will give you insight and inspire you to commence your project with confidence.</p>
      </div>
      <div class="photo photo--bedroom" role="img" aria-label="Calm bedroom with a made bed, bedside lamps and a balcony view"></div>
    </section>
  </main>
</body>
</html>
```